Business card design needed

www.marlonfab.com.au
Our primary services:
On-site welding.
On-site industrial maintenance.
On-site repairs and capital works projects specialising in pipe fabrication.
Our ability to work on-site with our dedicated mobile equipment is essential to our capability to provide a quality maintenance service to our customers. We are capable of providing a full team of qualified boilermakers that can work either to your plan or project manage if a plan has not been developed.
Industry/Entity Type
Industrial
Contact Information for Business Card
company name- MARLON FAB PTY LTD
story - industrial steel fabrication, constructions and pipelines
Director - Greg Hadley
workshop address - shed 7, 3862 kemble rd Tully
postal address - P.O BOX 628 WENDARRA Q 4867
mobile - 0429385106
w/shop phone - 0752937048
fax - 0752938159
email - admin@marlonfab.com.au
web - www.marlonfab.com.au
Logo Text
MARLON FAB pty ltd
Look and feel

```html
<!DOCTYPE html>
<html lang="en">
<head>
<meta charset="utf-8">
<title>Marlon Fab Business Cards</title>
<link href="https://fonts.googleapis.com/css2?family=Open+Sans:wght@400;600;700&display=swap" rel="stylesheet">
<style>
  :root {
    --stage-light: #ffffff;
    --stage-dark: #9a9a9a;
    --plate-black: #151515;
    --plate-edge: #2a2a2a;
    --panel-grey: #dcdcdc;
    --rule-white: #e8e8e8;
    --brand-violet: #4f4c9c;
    --ink-dark: #1e1e1e;
    --text-white: #ffffff;
  }
  * { margin: 0; padding: 0; box-sizing: border-box; }
  html, body { width: 1200px; height: 900px; overflow: hidden; }
  body {
    position: relative;
    font-family: "Open Sans", Arial, sans-serif;
    background: radial-gradient(ellipse 60% 60% at 40% 35%, var(--stage-light) 0%, #ececec 45%, var(--stage-dark) 100%);
  }
  .card {
    position: absolute;
    width: 514px;
    height: 291px;
    background: linear-gradient(135deg, #1e1e1e, var(--plate-black) 60%, #0c0c0c);
    border: 1px solid var(--plate-edge);
    box-shadow: 0 1px 3px rgba(0,0,0,.35);
    overflow: hidden;
  }
  .card-front { left: 30px; top: 294px; }
  .card-back-one { left: 648px; top: 110px; }
  .card-back-two { left: 648px; top: 456px; }

  .tagline {
    position: absolute; left: 0; right: 0; top: 30px;
    text-align: center; color: var(--text-white);
    font-size: 14px; letter-spacing: .1px;
  }
  .rule { position: absolute; left: 0; right: 0; height: 3px; background: var(--rule-white); }
  .rule-top { top: 62px; }
  .rule-bottom { top: 221px; }
  .info-panel {
    position: absolute; left: 0; right: 0; top: 72px; height: 144px;
    background: linear-gradient(180deg, #e4e4e4, var(--panel-grey));
  }
  .brand-name {
    position: absolute; font-weight: 700; letter-spacing: -.5px; line-height: 1;
    display: flex; align-items: center; gap: 8px;
  }
  .brand-name .mark { width: 14px; height: 14px; background: currentColor; }
  .front-brand { left: 16px; top: 54px; font-size: 28px; color: var(--brand-violet); }
  .back-brand { left: 14px; top: 24px; font-size: 23px; color: var(--text-white); }

  .person { position: absolute; left: 271px; top: 12px; color: var(--brand-violet); }
  .person-name { font-size: 18px; font-weight: 700; letter-spacing: .3px; line-height: 1.1; }
  .person-role { font-size: 11.5px; line-height: 1.2; }
  .contacts { list-style: none; margin-top: 10px; font-size: 12px; line-height: 15px; color: var(--ink-dark); }
  .contacts b { display: inline-block; width: 22px; color: var(--brand-violet); font-weight: 700; }

  .address {
    position: absolute; left: 0; right: 0; top: 238px;
    text-align: center; color: var(--text-white); font-size: 14.5px; line-height: 19px;
  }
  .photo-strips { position: absolute; inset: 0; }
</style>
</head>
<body>

<section class="card card-front">
  <p class="tagline">INDUSTRIAL STEEL FABRICATION, CONSTRUCTIONS AND PIPELINES</p>
  <div class="rule rule-top"></div>
  <div class="info-panel">
    <div class="brand-name front-brand"><span class="mark"></span>MARLON FAB</div>
    <div class="person">
      <p class="person-name">GREG HADLEY</p>
      <p class="person-role">Director</p>
      <ul class="contacts">
        <li><b>P:</b>0752 937 048</li>
        <li><b>F:</b>0752 938 159</li>
        <li><b>M:</b>0429 385 106</li>
        <li><b>E:</b>admin@marlonfab.com.au</li>
        <li><b>W:</b>www.marlonfab.com.au</li>
      </ul>
    </div>
  </div>
  <div class="rule rule-bottom"></div>
  <p class="address">SHED 7, 3862 KEMBLE RD WENDARRA<br>P.O BOX 628 WENDARRA Q 4867</p>
</section>

<section class="card card-back-one">
  <svg class="photo-strips" viewBox="0 0 514 291" width="514" height="291" role="img" aria-label="Photo of a welder working on a rusted pipe flange, cut into diagonal strips">
    <defs>
      <linearGradient id="flangeTones" x1="0" y1="0" x2="1" y2="1">
        <stop offset="0" stop-color="#6b6f78"/>
        <stop offset="0.45" stop-color="#3b4f8a"/>
        <stop offset="0.8" stop-color="#2d3f7a"/>
        <stop offset="1" stop-color="#c8662a"/>
      </linearGradient>
    </defs>
    <polygon points="215,0 297,0 185,291 103,291" fill="url(#flangeTones)"/>
    <polygon points="322,0 400,0 288,291 210,291" fill="url(#flangeTones)"/>
    <polygon points="425,0 514,0 514,40 400,291 313,291" fill="url(#flangeTones)"/>
  </svg>
  <div class="brand-name back-brand"><span class="mark"></span>MARLON FAB</div>
</section>

<section class="card card-back-two">
  <svg class="photo-strips" viewBox="0 0 514 291" width="514" height="291" role="img" aria-label="Photo of a gloved welder welding a large pipe bend with a bright arc, cut into diagonal strips">
    <defs>
      <linearGradient id="pipeTones" x1="0" y1="0" x2="1" y2="1">
        <stop offset="0" stop-color="#2c3550"/>
        <stop offset="0.4" stop-color="#b99a52"/>
        <stop offset="0.75" stop-color="#e8e2d6"/>
        <stop offset="1" stop-color="#8a7a4a"/>
      </linearGradient>
    </defs>
    <polygon points="215,0 297,0 185,291 103,291" fill="url(#pipeTones)"/>
    <polygon points="322,0 400,0 288,291 210,291" fill="url(#pipeTones)"/>
    <polygon points="425,0 514,0 514,40 400,291 313,291" fill="url(#pipeTones)"/>
  </svg>
  <div class="brand-name back-brand"><span class="mark"></span>MARLON FAB</div>
</section>

</body>
</html>
```